Bakery Business Cards

We are in need of business cards for our bakery business--something non-generic that reflects our business and will stand out. We are a wholesale bakery that primarily services in-store bakeries, casinos, schools, distributors, and fund-raising companies. The family business was founded in 1960. (www.marlowsovenworks.com)

```html
<!DOCTYPE html>
<html lang="en">
<head>
<meta charset="utf-8">
<title>Marlow's Ovenworks – Business Cards</title>
<link rel="stylesheet" href="https://fonts.googleapis.com/css2?family=Lato:wght@400;700;900&display=swap">
<style>
  :root {
    --backdrop: #cecece;
    --card-white: #ffffff;
    --brand-blue: #2f4ea6;
    --back-blue: #4561ab;
    --back-blue-deep: #3d58a2;
    --ink: #3f4250;
    --on-blue: #ffffff;
  }
  * { margin: 0; padding: 0; box-sizing: border-box; }
  html, body {
    width: 1200px;
    height: 800px;
    overflow: hidden;
    background: var(--backdrop);
    font-family: "Lato", Arial, sans-serif;
  }
  .stage { position: relative; width: 1200px; height: 800px; }

  .card {
    position: absolute;
    left: 390px;
    width: 420px;
    height: 240px;
    border-radius: 16px;
    overflow: hidden;
  }
  .card--front { top: 130px; background: var(--card-white); }
  .card--back { top: 430px; }

  /* Front */
  .front-wordmark {
    position: absolute;
    left: 22px;
    top: 82px;
    width: 160px;
    text-align: center;
    color: var(--brand-blue);
  }
  .front-wordmark .wordmark-name {
    display: block;
    font-weight: 900;
    font-size: 23px;
    line-height: 1.1;
  }
  .front-wordmark .wordmark-tagline {
    display: block;
    font-weight: 900;
    font-size: 11px;
    letter-spacing: 0.6px;
    margin-top: 5px;
  }
  .front-divider {
    position: absolute;
    left: 200px;
    top: 64px;
    width: 1px;
    height: 113px;
    background: var(--brand-blue);
  }
  .contact-block {
    position: absolute;
    left: 226px;
    top: 62px;
    color: var(--ink);
  }
  .contact-name {
    color: var(--brand-blue);
    font-weight: 700;
    font-size: 18px;
    letter-spacing: 0.2px;
    line-height: 1;
  }
  .contact-role {
    font-size: 11px;
    margin-top: 5px;
  }
  .contact-address {
    font-size: 11px;
    line-height: 14px;
    margin-top: 9px;
  }
  .contact-list {
    list-style: none;
    margin-top: 3px;
    font-size: 11px;
  }
  .contact-list li {
    display: flex;
    align-items: center;
    height: 15px;
  }
  .contact-icon {
    width: 10px;
    height: 10px;
    margin-right: 9px;
    flex: none;
  }

  /* Back */
  .back-photo {
    position: absolute;
    inset: 0;
    background: radial-gradient(ellipse at 50% 45%, var(--back-blue) 0%, var(--back-blue-deep) 100%);
  }
  .back-wordmark {
    position: absolute;
    left: 0;
    right: 0;
    top: 76px;
    text-align: center;
    color: var(--on-blue);
  }
  .back-wordmark .wordmark-name {
    display: block;
    font-weight: 900;
    font-size: 36px;
    line-height: 1.1;
  }
  .back-wordmark .wordmark-tagline {
    display: block;
    font-weight: 900;
    font-size: 14px;
    letter-spacing: 0.8px;
    margin-top: 6px;
  }
</style>
</head>
<body>
<main class="stage">

  <section class="card card--front" aria-label="Business card front">
    <div class="front-wordmark">
      <span class="wordmark-name">Marlow's<br>Ovenworks</span>
      <span class="wordmark-tagline">SINCE 1960</span>
    </div>
    <div class="front-divider"></div>
    <div class="contact-block">
      <h1 class="contact-name">DANIEL REYES</h1>
      <p class="contact-role">Founder &amp; CEO</p>
      <p class="contact-address">3172 Linden Ave,<br>Maple Falls, OK 73190</p>
      <ul class="contact-list">
        <li>
          <svg class="contact-icon" viewBox="0 0 24 24" aria-hidden="true">
            <path fill="var(--brand-blue)" d="M6.6 10.8a15.1 15.1 0 0 0 6.6 6.6l2.2-2.2a1 1 0 0 1 1-.25 11.4 11.4 0 0 0 3.6.57 1 1 0 0 1 1 1V20a1 1 0 0 1-1 1A17 17 0 0 1 3 4a1 1 0 0 1 1-1h3.5a1 1 0 0 1 1 1c0 1.25.2 2.45.57 3.57a1 1 0 0 1-.25 1z"/>
          </svg>
          (555) 310-4827
        </li>
        <li>
          <svg class="contact-icon" viewBox="0 0 24 24" aria-hidden="true">
            <rect x="2" y="5" width="20" height="14" fill="var(--brand-blue)"/>
            <path d="M2 5l10 8 10-8M2 19l7.5-7M22 19l-7.5-7" stroke="#fff" stroke-width="1.6" fill="none"/>
          </svg>
          sales@marlowsovenworks.com
        </li>
        <li>
          <svg class="contact-icon" viewBox="0 0 24 24" aria-hidden="true">
            <g fill="none" stroke="var(--brand-blue)" stroke-width="1.6">
              <circle cx="12" cy="12" r="10"/>
              <ellipse cx="12" cy="12" rx="4.5" ry="10"/>
              <path d="M2 12h20M4 7h16M4 17h16"/>
            </g>
          </svg>
          www.marlowsovenworks.com
        </li>
      </ul>
    </div>
  </section>

  <section class="card card--back" aria-label="Business card back">
    <div class="back-photo" role="img" aria-label="Blue-toned overhead photograph of pie slices and baked pastries on plates"></div>
    <div class="back-wordmark">
      <span class="wordmark-name">Marlow's<br>Ovenworks</span>
      <span class="wordmark-tagline">SINCE 1960</span>
    </div>
  </section>

</main>
</body>
</html>
```